Bright Harbor Capital website

Build a website template for the Bright Harbor Capital fund.
Looking for a cool website design showing companies we are using the latest in web design trends. We want to attract app developers, typically the younger set.
A good example of one of our competitive firms is http://mossfinch.org
The required components for the website include:
1) Funding application
2) about our firm
a) Partner profiles - We will include photographs and bios about each of the partners in our firm.
b) Invest with Bright Harbor - This will include information how to invest with our fund
c) our process - About our process for evaluating, funding and helping build successful businesses - This will include a narrative about the target companies, how we work, the type of deals we are interested in, our expectations, etc ...
3) Investment profiles - Stories about the companies we invest with
4) News - Output from our twitter feed and copies of our Blog posts

```html
<!DOCTYPE html>
<html lang="en">
<head>
<meta charset="utf-8">
<title>Bright Harbor Capital</title>
<link rel="stylesheet" href="https://fonts.googleapis.com/css2?family=Hind:wght@300;400;500;600&display=swap">
<style>
:root{
  --green:#5a9a12;
  --green-dark:#3f7a08;
  --ink:#3a3a3a;
  --muted:#666;
  --hero:#45443f;
  --hero-light:#5b5a55;
  --panel:#f6f5f5;
  --line:#d6d6d6;
  --band:#f1f1f1;
}
*{box-sizing:border-box;margin:0;padding:0}
html,body{width:856px;height:1200px;overflow:hidden;background:#fff}
body{position:relative;font-family:"Hind",Arial,sans-serif;color:var(--ink)}
.abs{position:absolute}

/* header */
.nav-bar{left:0;top:0;width:856px;height:50px;background:#fff}
.hero{left:0;top:50px;width:856px;height:265px;background:radial-gradient(ellipse at 62% 40%,var(--hero-light),var(--hero) 60%)}
.hero-visual{left:400px;top:100px;width:360px;height:215px;background:radial-gradient(ellipse at 50% 85%,#cfcfc6 0,#9c9d92 30%,rgba(69,68,63,0) 65%)}
.hero-grass{left:0;top:288px;width:420px;height:27px;background:linear-gradient(180deg,rgba(120,150,80,0),#6f8a4a)}
.logo-panel{left:0;top:0}
.brand{left:100px;top:30px;display:flex;align-items:center;gap:8px}
.brand-mark{width:26px;height:26px;border-radius:50%;background:var(--green)}
.brand-name{font-size:25px;font-weight:500;color:var(--green);line-height:1}
.brand-sub{left:134px;top:61px;font-size:10px;letter-spacing:3px;color:#777;font-weight:500}
.nav{left:375px;top:22px;display:flex;gap:11px;font-size:8.3px;color:#444;text-transform:uppercase;letter-spacing:-.1px}
.hero-title{left:118px;top:157px;font-size:20px;font-weight:300;color:#6fb01e}
.hero-sub{left:100px;top:184px;width:193px;text-align:right;font-size:11.5px;font-weight:300;color:#ddd;line-height:14px}
.dots{left:260px;top:222px;display:flex;gap:4px}
.dots span{width:7px;height:7px;background:#888}
.dots span:first-child{background:var(--green)}

/* section headings */
.h2{font-size:15px;font-weight:400;color:var(--ink);white-space:nowrap}
.h2 em{font-style:normal;color:var(--green)}
.rule{height:3px;border-top:1px dotted #bbb;border-bottom:1px dotted #bbb}

/* feature cards */
.card{left:104px;width:409px;height:124px;border:1px solid #e3e3e3;padding:4px}
.card-inner{width:100%;height:100%;background:var(--panel);display:flex}
.card-img{width:160px;height:114px;flex:none}
.card-text{padding:10px 0 0 16px;width:235px}
.card-text h3{font-size:11.5px;font-weight:400;margin-bottom:4px}
.card-text p{font-size:10.4px;line-height:14px;color:#555;font-weight:300}
.more{display:inline-block;margin-top:5px;font-size:10px;color:var(--green)}

/* form */
.field{left:533px;width:224px;border:1px solid #cfcfcf;background:#fafafa;font-size:11.5px;color:#555;padding:8px 7px;font-weight:300}
.submit{left:533px;top:537px;width:74px;height:33px;background:linear-gradient(#5ea019,#3e7c0a);color:#fff;font-size:11.5px;display:flex;align-items:center;justify-content:center}
.dash{left:533px;width:223px;border-top:1px dashed #c9c9c9}

/* partners */
.partner{left:533px;width:225px;display:flex;gap:10px}
.partner-img{width:58px;height:48px;flex:none;background:linear-gradient(135deg,#e8e3da,#6e6252)}
.partner p{font-size:8.6px;line-height:13.5px;color:#555;padding-top:0}
.partner p b{display:block;color:var(--green);font-weight:400}
.partner p i{font-style:normal;color:#222}

/* investment logos */
.tile{top:803px;width:69px;height:69px;border:1px solid #d5d5d5;padding:3px}
.tile div{width:100%;height:100%;background:radial-gradient(#fff 30%,#d8d8d8);display:flex;align-items:center;justify-content:center;font-size:11px;font-weight:500;color:#444}

/* blog band */
.band{left:0;top:906px;width:856px;height:229px;background:var(--band)}
.post{left:104px;display:flex;gap:13px}
.date{width:51px;height:50px;border:2px solid #dcdcdc;background:linear-gradient(#4e9212,#2f6a05);color:#fff;text-align:center;padding-top:6px;flex:none}
.date b{display:block;font-size:16px;font-weight:400;line-height:17px}
.date span{font-size:9.5px}
.post-text{font-size:8.6px;line-height:12.8px;color:#555;width:330px}
.post-text h4{font-weight:400;color:var(--green);font-size:9px;margin-bottom:2px}
.post-text i{font-style:normal;color:#333}

.tweet{left:532px;top:931px;width:225px;height:170px;background:#fff;border:1px solid #dedede}
.tw-sq{left:11px;top:50px;width:32px;height:32px;background:#2a7ec0}
.tw-pic{top:92px;width:64px;height:63px}

.footer{left:104px;top:1159px;display:flex;gap:13px;font-size:8.5px;color:#444}
.copy{left:626px;top:1159px;font-size:8.5px;color:#444}
.copy em{font-style:normal;color:var(--green)}
</style>
</head>
<body>

<div class="abs nav-bar"></div>
<div class="abs hero"></div>
<div class="abs hero-visual" role="img" aria-label="Young plant growing from a pile of banknotes in front of a faint globe"></div>
<div class="abs hero-grass" role="img" aria-label="Grass along the lower edge of the banner"></div>

<svg class="abs logo-panel" width="380" height="102" viewBox="0 0 380 102">
  <polygon points="0,0 368,0 295,101 0,101" fill="#f4f4f4"/>
  <polyline points="368,0 295,101 0,101" fill="none" stroke="#d8d8d8" stroke-width="1"/>
  <line x1="370" y1="0" x2="298" y2="100" stroke="#2a2a2a" stroke-width="3"/>
</svg>

<div class="abs brand"><span class="brand-mark"></span><span class="brand-name">Bright Harbor</span></div>
<div class="abs brand-sub">CAPITAL</div>

<nav class="abs nav">
  <span>Funding Application</span><span>About Us</span><span>Invest with us</span><span>Partners</span><span>Process</span><span>Profiles</span><span>News</span>
</nav>

<div class="abs hero-title">Welcome to our site</div>
<div class="abs hero-sub">Evaluating, funding and helping build successful businesses</div>
<div class="abs dots"><span></span><span></span><span></span></div>

<!-- left column -->
<div class="abs h2" style="left:105px;top:354px"><em>About</em> Us</div>
<div class="abs rule" style="left:182px;top:362px;width:330px"></div>
<div class="abs card" style="top:386px">
  <div class="card-inner">
    <div class="card-img" role="img" aria-label="Portrait of a partner in a coat" style="background:linear-gradient(90deg,#ece6da,#8b7a62 55%,#efe9de)"></div>
    <div class="card-text"><h3>Know who we are</h3><p>Lorem ipsum dolor sit amet, consectetur adipisicing elit, sed do eiusmod tempor incididunt ut labore et dolore magna aliqua.</p><span class="more">Read More &gt;</span></div>
  </div>
</div>

<div class="abs h2" style="left:105px;top:538px"><em>Invest with</em> Bright Harbor</div>
<div class="abs rule" style="left:263px;top:546px;width:249px"></div>
<div class="abs card" style="top:567px">
  <div class="card-inner">
    <div class="card-img" role="img" aria-label="Business people reviewing charts on a tablet" style="background:linear-gradient(135deg,#3b4a63,#dfe6ee 50%,#2f8ed0)"></div>
    <div class="card-text"><h3>How to invest with our fund</h3><p>Lorem ipsum dolor sit amet, consectetur adipisicing elit, sed do eiusmod tempor incididunt ut labore et dolore magna aliqua.</p><span class="more">Read More &gt;</span></div>
  </div>
</div>

<div class="abs h2" style="left:105px;top:718px"><em>Investment</em>&nbsp; Process</div>
<div class="abs rule" style="left:249px;top:726px;width:263px"></div>
<div class="abs card" style="top:747px">
  <div class="card-inner">
    <div class="card-img" role="img" aria-label="Laptop showing a bar chart in a meeting" style="background:linear-gradient(135deg,#5a4636,#b9bec4 50%,#3e3a36)"></div>
    <div class="card-text"><h3>3 step process to investment</h3><p>Lorem ipsum dolor sit amet, consectetur adipisicing elit, sed do eiusmod tempor incididunt ut labore et dolore magna aliqua.</p><span class="more">Read More &gt;</span></div>
  </div>
</div>

<!-- right column -->
<div class="abs h2" style="left:534px;top:354px"><em>Request for</em> Financing</div>
<div class="abs field" style="top:385px;height:33px">Name</div>
<div class="abs field" style="top:423px;height:33px">Email id</div>
<div class="abs field" style="top:460px;height:69px">Query</div>
<div class="abs submit">Submit</div>
<div class="abs dash" style="top:592px"></div>

<div class="abs h2" style="left:534px;top:608px"><em>Partner</em> Profiles</div>
<div class="abs partner" style="top:633px">
  <div class="partner-img" role="img" aria-label="Partner portrait"></div>
  <p><b>Owen Castell,</b>We will include photographs and bios about each of the partners in our firm. <i>Read More &gt;&gt;</i></p>
</div>
<div class="abs partner" style="top:699px">
  <div class="partner-img" role="img" aria-label="Partner portrait"></div>
  <p><b>Owen Castell,</b>We will include photographs and bios about each of the partners in our firm. <i>Read More &gt;&gt;</i></p>
</div>

<div class="abs h2" style="left:534px;top:775px"><em>Investment</em> Profiles</div>
<div class="abs tile" style="left:535px"><div>Veltrix</div></div>
<div class="abs tile" style="left:610px"><div>Markly</div></div>
<div class="abs tile" style="left:686px"><div>Quorra</div></div>

<!-- blog band -->
<div class="abs band"></div>
<div class="abs h2" style="left:105px;top:939px">Our Blog</div>
<div class="abs" style="left:104px;top:968px;width:408px;border-top:1px dashed #c5c5c5"></div>

<div class="abs post" style="top:984px">
  <div class="date"><b>12</b><span>JAN</span></div>
  <div class="post-text"><h4>Blog headline1</h4>Lorem ipsum dolor sit amet, consectetur adipisicing elit, sed do eiusmod tempor incididunt ut labore et dolore magna aliqua.<br><i>Read Details &gt;</i></div>
</div>
<div class="abs post" style="top:1050px">
  <div class="date"><b>26</b><span>JAN</span></div>
  <div class="post-text"><h4>Blog headline2</h4>Lorem ipsum dolor sit amet, consectetur adipisicing elit, sed do eiusmod tempor incididunt ut labore et dolore magna aliqua.<br><i>Read Details &gt;</i></div>
</div>

<div class="abs tweet">
  <div class="abs h2" style="left:12px;top:9px">Tweet Us</div>
  <div class="abs" style="left:11px;top:36px;width:202px;border-top:1px dashed #ccc"></div>
  <div class="abs tw-sq"></div>
  <div class="abs" style="left:50px;top:50px;font-size:9.5px;color:#444">31213 Followers</div>
  <svg class="abs" style="left:50px;top:68px" width="11" height="10" viewBox="0 0 11 10"><path d="M1 4h2v6H1zM4 4l2-4c1 0 1.5.6 1.3 2L7 4h3c.6 0 1 .5.8 1l-1 4c-.1.6-.5 1-1 1H4z" fill="#2a7ec0"/></svg>
  <div class="abs" style="left:65px;top:66px;font-size:9.5px;color:#444;text-decoration:underline">Tweet Us</div>
  <div class="abs tw-pic" style="left:11px;background:linear-gradient(135deg,#c9b6a6,#8a2a2a)" role="img" aria-label="Follower photo"></div>
  <div class="abs tw-pic" style="left:81px;background:linear-gradient(135deg,#dfe3e8,#6f7f92)" role="img" aria-label="Follower photo"></div>
  <div class="abs tw-pic" style="left:151px;background:linear-gradient(135deg,#bfe3ee,#3a2a22)" role="img" aria-label="Follower photo"></div>
</div>

<div class="abs footer"><span>Funding application</span><span>About Us</span><span>Invest with us</span><span>Partners</span><span>process</span><span>profiles</span><span>News</span></div>
<div class="abs copy">Copyright@2014, <em>Bright Harbor</em></div>

</body>
</html>
```